Packaging Design for "Out-along" healthy snack

We are a young trading company based in Melaka, Malaysia. Our product range include healthy snack food products such as;
1. Dried fruit (Raisin, Date and Apricot)
2. Nuts (Almond, walnut and Pitstachio)

Our Brand name is - Out-Along (registrated mark)
Motto: Healthy snacks that everyone will craved out-Along meal time.

Target market segment:
1. Night life business such as Pub, Lounge, Kara-oke
2. Vegetarian and Health food restaurant
3. Appetiser for Premium Restaurant

Packs size : 100g, 250g and 500g

Packing type: Screw Cap Jar (Square L7.5cm X W7.5cm X H9.0cm)

Competitor website:
http://www.plakorvanel.example/index.php?ws=ourproducts&cat=Nuts#openproducts

https://grivoltasp.example/driedfruit/ (For company philosophy)

KMTarvu
kelbrimo@quadrelmail.example

Vorelix Tarn (M) Sdn. Bhd. (owner of Out-along brand)

Target Market(s)

Customer that have middle and high income that have disposable budget for healthy and good taste snack in between meal time. Those business man that like to meet client at the night life outlets would enjoy our snacks

Industry/Entity Type

It Company

Font styles to use
Sans Serif

Colors
faa54b
886aae
87cfc6

Requirements
Must have
• 1. Out-along as brand name
• 2. Product names area
• 3. Die cut window that let consumer see the product inside
• 4. Nutritional facts and Ingredients
Nice to have
• 1. A attractive logo for "Out-along" brand

```html
<!DOCTYPE html>
<html lang="en">
<head>
<meta charset="utf-8">
<title>Out-along Pistachio Nuts – Jar Label</title>
<link rel="stylesheet" href="https://fonts.googleapis.com/css2?family=Lato:wght@300;400;700&family=Kaushan+Script&family=Dancing+Script:wght@600&family=Arimo:ital,wght@0,400;0,700;1,400&display=swap">
<style>
  :root {
    --page-bg: #e8e5e0;
    --label-purple: #7652ab;
    --label-purple-light: #8b6bb8;
    --label-purple-dark: #5e3c94;
    --window-rim: #5b3a91;
    --accent-orange: #faa54b;
    --nut-cream: #d8d0b0;
    --white: #ffffff;
    --ink: #111111;
  }
  * { box-sizing: border-box; margin: 0; padding: 0; }
  html, body { width: 1200px; height: 900px; overflow: hidden; }
  body { background: var(--page-bg); position: relative; font-family: "Lato", sans-serif; }

  .jar-label {
    position: absolute; left: 50px; top: 235px; width: 1100px; height: 430px; overflow: hidden;
    background: radial-gradient(ellipse at 50% 60%, var(--label-purple-light) 0%, var(--label-purple) 55%, var(--label-purple-dark) 100%);
    color: var(--white);
  }
  .label-shapes { position: absolute; inset: 0; width: 100%; height: 100%; }

  .ingredients { position: absolute; left: 30px; top: 36px; width: 250px; text-align: center; }
  .ingredients h2 { font-size: 19px; font-weight: 700; line-height: 24px; }
  .ingredients p { font-size: 19px; font-weight: 300; line-height: 24.5px; }

  .dates { position: absolute; left: 30px; top: 204px; width: 250px; text-align: center; font-size: 19px; font-weight: 300; line-height: 24px; }
  .dates .date-field { display: block; width: 168px; height: 18px; margin: 4px auto 4px; background: var(--white); border-radius: 9px; }

  .claims { position: absolute; left: 55px; top: 332px; display: flex; gap: 6px; list-style: none; }
  .claim { width: 37px; text-align: center; }
  .claim span { display: block; font-size: 5px; font-weight: 700; white-space: nowrap; margin-bottom: 8px; }
  .claim i { display: block; width: 30px; height: 30px; margin: 0 auto; border: 2.5px solid var(--white); border-radius: 50%; }

  .variant { position: absolute; left: 361px; top: 252px; width: 360px; text-align: center; font-size: 40px; font-weight: 300; line-height: 50px; letter-spacing: 0.5px; }
  .product-name { position: absolute; left: 280px; top: 300px; width: 530px; text-align: center; font-family: "Kaushan Script", cursive; font-weight: 400; font-size: 78px; line-height: 100px; }

  .promise { position: absolute; left: 682px; top: 215px; width: 103px; height: 103px; border-radius: 50%; background: var(--accent-orange);
    display: flex; align-items: center; justify-content: center; text-align: center; padding: 12px;
    font-family: "Dancing Script", cursive; font-size: 14px; line-height: 17px; }

  .nutrition { position: absolute; left: 815px; top: 46px; width: 219px; height: 338px; background: var(--white); padding: 6px; }
  .nutrition-box { border: 2px solid var(--ink); height: 100%; padding: 3px 5px; color: var(--ink); font-family: "Arimo", sans-serif; font-size: 9px; }
  .nutrition h3 { font-size: 23px; font-weight: 700; line-height: 24px; letter-spacing: -0.3px; }
  .nutrition .serving { font-size: 8.5px; line-height: 10px; }
  .nutrition .bar-thick { height: 10px; background: var(--ink); margin: 4px 0 3px; }
  .nutrition .row { display: flex; justify-content: space-between; border-top: 1px solid var(--ink); padding: 2px 0; line-height: 12px; }
  .nutrition .row.first { border-top: none; }
  .nutrition .row.heavy { border-top-width: 3px; }
  .nutrition .sub { padding-left: 10px; }
  .nutrition .small { font-size: 6px; line-height: 9px; }
  .nutrition .right-small { justify-content: flex-end; font-size: 6px; font-weight: 700; }
  .nutrition .footnote { border-top: 1px solid var(--ink); font-size: 6px; line-height: 8px; padding-top: 3px; }
  .nutrition .dot { font-size: 9px; }
</style>
</head>
<body>
  <main class="jar-label">
    <svg class="label-shapes" viewBox="0 0 1257 492" preserveAspectRatio="none">
      <defs>
        <linearGradient id="nutFill" x1="0" y1="0" x2="1" y2="1">
          <stop offset="0" stop-color="#e2dcc0"/>
          <stop offset="0.5" stop-color="#d8d0b0"/>
          <stop offset="1" stop-color="#a89c78"/>
        </linearGradient>
        <radialGradient id="clusterFill" cx="0.5" cy="0.5" r="0.6">
          <stop offset="0" stop-color="#f2c98a"/>
          <stop offset="1" stop-color="#d99a55"/>
        </radialGradient>
      </defs>
      <path class="product-window" role="img" aria-label="Die-cut window showing the roasted pistachios inside the jar"
        d="M402 200 C396 120 440 62 520 50 C640 40 760 44 805 84 C845 124 838 205 832 288 C760 254 610 238 525 246 C460 252 408 248 402 200 Z"
        fill="url(#nutFill)" stroke="#5b3a91" stroke-width="9"/>
      <ellipse class="nut-cluster" role="img" aria-label="Illustration of a small heap of pistachios in shells"
        cx="418" cy="242" rx="95" ry="50" fill="url(#clusterFill)"/>
    </svg>

    <section class="ingredients">
      <h2>Ingredients:</h2>
      <p>Pistachios, salt, pepper, sugar, onion powder, garlic powder, dextrose, lemon juice concentrate, rosemary extract and yeast extract.</p>
    </section>

    <section class="dates">
      <p>Expiry Date:</p>
      <span class="date-field"></span>
      <p>Date manufacturing:</p>
    </section>

    <ul class="claims">
      <li class="claim"><span>VEGETARIAN</span><i></i></li>
      <li class="claim"><span>READY TO EAT</span><i></i></li>
      <li class="claim"><span>FAIR TRADE</span><i></i></li>
      <li class="claim"><span>NO COLORING</span><i></i></li>
      <li class="claim"><span>NO SUGAR &amp; MSG</span><i></i></li>
    </ul>

    <p class="variant">(out-along)</p>
    <h1 class="product-name">Pistachio Nuts</h1>

    <p class="promise">Made from ingredients that you can spell</p>

    <section class="nutrition">
      <div class="nutrition-box">
        <h3>Nutrition Facts</h3>
        <p class="serving">Serving Size 1 Rounded Scoop (33g)<br>Servings Per Container 45</p>
        <div class="bar-thick"></div>
        <div class="row first small"><strong>Amount Per Serving</strong></div>
        <div class="row heavy"><span><strong>Calories</strong> 130</span><span>Calories from Fat 20</span></div>
        <div class="row right-small"><span>% Daily Value*</span></div>
        <div class="row heavy"><span><strong>Total Fat</strong> 2g</span><span>3%</span></div>
        <div class="row sub"><span>Saturated Fat 1g</span><span>5%</span></div>
        <div class="row sub"><span><em>Trans</em> Fat 0g</span><span></span></div>
        <div class="row"><span><strong>Cholestrol</strong> 60mg</span><span>20%</span></div>
        <div class="row"><span><strong>Sodium</strong> 210mg</span><span>9%</span></div>
        <div class="row"><span><strong>Total Carbohydrate</strong> 4g</span><span>1%</span></div>
        <div class="row sub"><span>Sugars 2g</span><span></span></div>
        <div class="row"><span><strong>Protein</strong> 24g</span><span>48%</span></div>
        <div class="bar-thick"></div>
        <div class="row first"><span>Vitamin A 0%</span><span class="dot">•</span><span>Vitamin C 0%</span></div>
        <div class="row"><span>Calcium 8%</span><span class="dot">•</span><span>Iron 2%</span></div>
        <p class="footnote">Not a Significant Source of Dietary Fiber<br>*Percent Daily Values are based on a 2,000 calorie diet.</p>
      </div>
    </section>
  </main>
</body>
</html>
```